Transit Van Vehicle Wrap for Fenwick Meadow Gardens

We need to wrap two of our transit vans. One is a replacement. The old wrap had a back patio scene with patio furniture and lanscaping. Im not sure this is what we want moving forward. I want people to easily identify it is Fenwick Meadow Gardens when they look at the vehicle. Most recently we have wrapped our landscape trailers black, however with the base color being white and not wanting to wrap all of the vehicle, Im not sure black background is the way to go. We've also considered using 3 or 4 picture windows and a subtitle to describe what we do. We can to list words like Container Gardening, Backyard Patios, Houseplants, Plant Doctors, etc. instead of using department names to tell people what we do. We would like to use more specific words and words that formulate an image in your mind when you say it. Needs to have our logo in it. Sides and Rear doors. Rear should be logo with words or services listed. The sides could be the same or images. Ive attached two logos, one meant to be used overtop of darker background. We are a retail lifestyle garden center and landscape design build company, selling annuals, perennial, trees shrubs, lawn care items, gardening tools, house plants, pottery, patio furniture, mens and womens apparel and accessories, christmas decor and trees, lorne candles and other home fragrence, seasonal home decor and more. Visit fenwickmeadowgardens.com to see it all.

Target Market(s)

Home Owners in their 40s to 50s

Industry/Entity Type

lifestyle garden center and landscape firm

Requirements
Must have
• company logo and words describing what we do.

```html
<!DOCTYPE html>
<html lang="en">
<head>
<meta charset="utf-8">
<title>Fenwick Meadow Gardens – Transit Van Wrap</title>
<link rel="stylesheet" href="https://fonts.googleapis.com/css2?family=Ubuntu:wght@400;500;700&display=swap">
<style>
  :root {
    --stage: #1b1b1b;
    --van-white: #f7f7f5;
    --leaf-green: #7cb342;
    --deep-green: #2e5d1f;
    --sun-yellow: #f2d43a;
    --petal-pink: #d9407a;
    --bloom-red: #b3213a;
    --ink-white: #ffffff;
    --rocker-grey: #8a8a8a;
  }
  html, body {
    margin: 0;
    padding: 0;
    width: 1200px;
    height: 2649px;
    overflow: hidden;
    background: var(--stage);
    font-family: "Ubuntu", sans-serif;
  }
  .canvas { position: relative; width: 1200px; height: 2649px; }
  .panel { position: absolute; display: block; }
  .side-driver { left: 50px; top: 60px; }
  .side-passenger { left: 50px; top: 680px; }
  .rear-doors { left: 150px; top: 1320px; }
  .brand-name { font-family: "Ubuntu", sans-serif; font-weight: 700; fill: var(--deep-green); }
  .phone { font-family: "Ubuntu", sans-serif; font-weight: 700; fill: var(--ink-white); }
  .web { font-family: "Ubuntu", sans-serif; font-weight: 500; fill: var(--ink-white); }
  .welcome { font-family: "Ubuntu", sans-serif; font-weight: 500; fill: var(--sun-yellow); }
  .service { font-family: "Ubuntu", sans-serif; font-weight: 400; fill: var(--ink-white); }
</style>
</head>
<body>
<div class="canvas">
  <svg width="0" height="0" style="position:absolute">
    <defs>
      <linearGradient id="flowerBed" x1="0" y1="0" x2="1" y2="1">
        <stop offset="0" stop-color="#3f6b2a"/>
        <stop offset="0.45" stop-color="#c7416f"/>
        <stop offset="0.75" stop-color="#8e2a3c"/>
        <stop offset="1" stop-color="#2f5522"/>
      </linearGradient>
      <linearGradient id="flowerStrip" x1="0" y1="0" x2="1" y2="0">
        <stop offset="0" stop-color="#c5477d"/>
        <stop offset="0.5" stop-color="#3d6a2b"/>
        <stop offset="1" stop-color="#d0557f"/>
      </linearGradient>
      <radialGradient id="glassOval" cx="0.5" cy="0.5" r="0.6">
        <stop offset="0" stop-color="#cfe3e6"/>
        <stop offset="1" stop-color="#7fb3b8"/>
      </radialGradient>
    </defs>
  </svg>

  <!-- Driver side -->
  <svg class="panel side-driver" width="1100" height="560" viewBox="0 0 1100 560">
    <rect x="0" y="0" width="1100" height="560" rx="18" fill="var(--van-white)"/>
    <polygon points="250,560 370,400 830,400 1000,0 1100,0 1100,560" fill="url(#flowerBed)" role="img" aria-label="Photo of pink geraniums and red flowers in garden beds"/>
    <polyline points="230,560 352,400" stroke="var(--sun-yellow)" stroke-width="10" fill="none"/>
    <polyline points="815,400 985,0" stroke="var(--sun-yellow)" stroke-width="10" fill="none"/>
    <rect x="0" y="510" width="1100" height="50" fill="url(#flowerStrip)" role="img" aria-label="Strip of mixed flower blooms along the lower body"/>
    <circle cx="300" cy="190" r="26" fill="var(--sun-yellow)"/>
    <text class="brand-name" x="345" y="208" font-size="50">Fenwick Meadow Gardens</text>
    <g role="img" aria-label="Row of six round photos of staff, plants, patio and greenhouse">
      <circle cx="430" cy="320" r="30" fill="#c99a6b"/>
      <circle cx="505" cy="320" r="30" fill="#e0b436"/>
      <circle cx="580" cy="320" r="30" fill="#8a9b8c"/>
      <circle cx="655" cy="320" r="30" fill="#e6e6df"/>
      <circle cx="730" cy="320" r="30" fill="#a8c79a"/>
      <circle cx="805" cy="320" r="30" fill="#c9d4d0"/>
    </g>
    <text class="phone" x="380" y="448" font-size="38">+1 555-014-2290</text>
    <text class="web" x="392" y="480" font-size="22">fenwickmeadowgardens.com</text>
    <text class="welcome" x="1075" y="438" font-size="20" text-anchor="end">Welcome to Fenwick Meadow Gardens</text>
    <text class="welcome" x="1075" y="464" font-size="20" text-anchor="end">where imaginations grow!</text>
    <g fill="var(--leaf-green)">
      <circle cx="95" cy="310" r="11"/>
      <circle cx="123" cy="310" r="11"/>
      <circle cx="151" cy="310" r="11"/>
    </g>
    <circle cx="230" cy="340" r="55" fill="var(--sun-yellow)"/>
  </svg>

  <!-- Passenger side -->
  <svg class="panel side-passenger" width="1100" height="560" viewBox="0 0 1100 560">
    <rect x="0" y="0" width="1100" height="560" rx="18" fill="var(--van-white)"/>
    <polygon points="850,560 730,400 270,400 100,0 0,0 0,560" fill="url(#flowerBed)" role="img" aria-label="Photo of pink geraniums and red flowers in garden beds"/>
    <polyline points="870,560 748,400" stroke="var(--sun-yellow)" stroke-width="10" fill="none"/>
    <polyline points="285,400 115,0" stroke="var(--sun-yellow)" stroke-width="10" fill="none"/>
    <rect x="0" y="510" width="1100" height="50" fill="url(#flowerStrip)" role="img" aria-label="Strip of mixed flower blooms along the lower body"/>
    <circle cx="200" cy="190" r="26" fill="var(--sun-yellow)"/>
    <text class="brand-name" x="245" y="208" font-size="50">Fenwick Meadow Gardens</text>
    <g role="img" aria-label="Row of six round photos of staff, plants, patio and greenhouse">
      <circle cx="300" cy="320" r="30" fill="#c99a6b"/>
      <circle cx="375" cy="320" r="30" fill="#e0b436"/>
      <circle cx="450" cy="320" r="30" fill="#8a9b8c"/>
      <circle cx="525" cy="320" r="30" fill="#e6e6df"/>
      <circle cx="600" cy="320" r="30" fill="#a8c79a"/>
      <circle cx="675" cy="320" r="30" fill="#c9d4d0"/>
    </g>
    <text class="phone" x="440" y="448" font-size="38">+1 555-014-2290</text>
    <text class="web" x="452" y="480" font-size="22">fenwickmeadowgardens.com</text>
    <text class="welcome" x="30" y="438" font-size="20">Welcome to Fenwick Meadow Gardens</text>
    <text class="welcome" x="60" y="464" font-size="20">where imaginations grow!</text>
    <g fill="var(--leaf-green)">
      <circle cx="949" cy="310" r="11"/>
      <circle cx="977" cy="310" r="11"/>
      <circle cx="1005" cy="310" r="11"/>
    </g>
    <circle cx="870" cy="340" r="55" fill="var(--sun-yellow)"/>
  </svg>

  <!-- Rear doors -->
  <svg class="panel rear-doors" width="900" height="1100" viewBox="0 0 900 1100">
    <rect x="0" y="0" width="900" height="1100" rx="24" fill="url(#flowerBed)" role="img" aria-label="Photo of pink and white impatiens with green foliage"/>
    <line x1="450" y1="0" x2="450" y2="1100" stroke="#1e1e1e" stroke-width="4"/>
    <ellipse cx="450" cy="330" rx="380" ry="210" fill="url(#glassOval)" role="img" aria-label="Stained glass garden ornament"/>
    <text class="welcome" x="450" y="70" font-size="32" text-anchor="middle">Welcome to Fenwick Meadow Gardens</text>
    <text class="welcome" x="450" y="110" font-size="32" text-anchor="middle">where imaginations grow!</text>
    <circle cx="125" cy="366" r="26" fill="var(--sun-yellow)"/>
    <text class="brand-name" x="168" y="384" font-size="50">Fenwick Meadow Gardens</text>
    <text class="phone" x="40" y="650" font-size="44">+1 555-014-2290</text>
    <text class="web" x="860" y="645" font-size="24" text-anchor="end">fenwickmeadowgardens.com</text>
    <g class="service" font-size="32">
      <text x="40" y="730">• Container Gardening</text>
      <text x="40" y="785">• Backyard Patios</text>
      <text x="40" y="840">• Houseplants</text>
      <text x="40" y="895">• Plant Doctors, etc.</text>
    </g>
    <circle cx="740" cy="850" r="110" fill="var(--sun-yellow)"/>
  </svg>
</div>
</body>
</html>
```